Two (2) Merchant Advance Banner Ads

I need two (2) ads with rotating gif with 3 transitions for http://fundlinker.com/

Ad Specs:
Ad 1 must be an image equal to 250x250 pixels for website and email newsletter. .jpg, .gif, and
.png okay. No Flash!

Ad 2 must be an image equal to 720x90 pixels for website and mobile device view. .jpg, .gif, and
.png only. No Flash!

Client: Harwick Funding Partners merchant cash advance company out of Chicago. They provide alternative (to a bank loan) financing for small business owners across the U.S.
Here's their website: www.harwickfp.com

Purpose: Recruit 3rd party sellers of alternative financing. There are many sales financing professionals already out there soliciting small businesses, we want them to make a decision to sell Harwick's financing product to small businesses.

Copy:
Real People.
Competitive Commissions.
Great Rates.

I would like the logo (attached), phone number and CTA button to appear on all three transitions.
Call (888) 417-2859
Button: Get Started

Style:
Either something clean and simple, or something similar (not identifcal) to ads attached.
Brand standards guide is attached. Please use colors from guide.

```html
<!DOCTYPE html>
<html lang="en">
<head>
<meta charset="utf-8">
<title>Harwick Funding Partners – Recruiting Banner Frames</title>
<link rel="stylesheet" href="https://fonts.googleapis.com/css2?family=Montserrat:wght@300;400;600;700;800&display=swap">
<style>
  :root {
    --stage: #000000;
    --lime: #b6c535;
    --lime-glow: #e2ea9a;
    --lime-text: #8db63c;
    --navy: #4b4f70;
    --teal: #18a2b2;
    --white: #ffffff;
    --bubble: #f7f7f4;
    --logo-grey: #4e5360;
    --label: #ffffff;
  }
  * { box-sizing: border-box; margin: 0; padding: 0; }
  html, body {
    width: 1200px; height: 450px; overflow: hidden;
    background: var(--stage);
    font-family: "Montserrat", Arial, sans-serif;
  }
  .board { position: relative; width: 1200px; height: 450px; }

  .frame {
    position: absolute; top: 29px;
    width: 360px; height: 360px; overflow: hidden;
    background: radial-gradient(circle at 95px 170px, var(--lime-glow) 0%, var(--lime) 55%);
  }
  .frame--one { left: 33px; }
  .frame--two { left: 418px; }
  .frame--three { left: 803px; }

  .frame-label {
    position: absolute; top: 406px; width: 360px;
    text-align: center; color: var(--label);
    font-weight: 300; font-size: 20px; letter-spacing: 0.5px;
  }

  .character {
    position: absolute; left: 14px; top: 14px; width: 190px; height: 300px;
    border-radius: 90px 90px 20px 20px;
    background: linear-gradient(180deg, #c8d36a 0%, #dfe2d8 45%, #d6d8d4 80%, #3b3a3a 100%);
    opacity: 0.75;
  }

  .bubble {
    position: absolute; background: var(--bubble);
    border-radius: 12px; text-transform: uppercase;
    box-shadow: 2px 3px 5px rgba(0,0,0,0.18);
    line-height: 1;
  }
  .bubble::before {
    content: ""; position: absolute; width: 0; height: 0;
    border-style: solid;
  }
  .bubble__strong { display: block; font-weight: 800; }
  .bubble__light { display: block; font-weight: 300; }

  .bubble--people { left: 191px; top: 15px; width: 115px; height: 67px; padding: 12px 0 0 17px; color: var(--lime-text); }
  .bubble--people .bubble__strong { font-size: 25px; }
  .bubble--people .bubble__light { font-size: 18px; margin-top: 1px; }
  .bubble--people::before { left: -10px; bottom: 10px; border-width: 8px 12px 0 0; border-color: transparent var(--bubble) transparent transparent; }

  .bubble--commissions { left: 218px; top: 95px; width: 160px; height: 72px; padding: 21px 0 0 14px; color: var(--navy); }
  .bubble--commissions .bubble__strong { font-size: 15px; }
  .bubble--commissions .bubble__light { font-size: 13.5px; margin-top: 3px; }
  .bubble--commissions::before { left: -14px; top: 20px; border-width: 0 14px 10px 0; border-color: transparent var(--bubble) transparent transparent; }

  .bubble--rates { left: 179px; top: 178px; width: 142px; height: 75px; padding: 13px 0 0 29px; color: #a9c34d; }
  .bubble--rates .bubble__strong { font-size: 25px; }
  .bubble--rates .bubble__light { font-size: 25px; margin-top: 2px; }
  .bubble--rates::before { left: -14px; top: 14px; border-width: 0 14px 10px 0; border-color: transparent var(--bubble) transparent transparent; }

  .call {
    position: absolute; left: 153px; width: 194px; top: 264px;
    text-align: center; color: var(--white);
  }
  .call__label { display: block; font-size: 12px; font-weight: 400; letter-spacing: 4px; }
  .call__number { display: block; font-size: 18px; font-weight: 700; margin-top: 3px; }

  .cta {
    position: absolute; left: 153px; top: 307px; width: 194px; height: 39px;
    background: var(--teal); color: var(--white); border-radius: 5px;
    font-size: 22px; font-weight: 700; text-align: center; line-height: 39px;
    box-shadow: 2px 3px 4px rgba(0,0,0,0.2);
  }

  .logo-band { position: absolute; left: 0; bottom: 0; width: 170px; height: 90px; }
  .brand-name {
    position: absolute; left: 14px; top: 310px; width: 125px;
    color: var(--logo-grey); font-size: 14px; font-weight: 600; line-height: 1.15;
  }
</style>
</head>
<body>
<main class="board">

  <section class="frame frame--one" aria-label="Frame 1">
    <div class="character" role="img" aria-label="Illustrated businessman with glasses and tie, raising one finger"></div>
    <div class="bubble bubble--people"><span class="bubble__strong">Real</span><span class="bubble__light">People.</span></div>
    <svg class="logo-band" viewBox="0 0 170 90" aria-hidden="true"><path d="M0 90 V40 Q70 -5 170 55 V90 Z" fill="#ffffff"/></svg>
    <p class="brand-name">Harwick Funding Partners</p>
    <p class="call"><span class="call__label">Call</span><span class="call__number">(844) 312-7740</span></p>
    <a class="cta">GET STARTED</a>
  </section>

  <section class="frame frame--two" aria-label="Frame 2">
    <div class="character" role="img" aria-label="Illustrated businessman with glasses and tie, raising two fingers"></div>
    <div class="bubble bubble--people"><span class="bubble__strong">Real</span><span class="bubble__light">People.</span></div>
    <div class="bubble bubble--commissions"><span class="bubble__strong">Competitive</span><span class="bubble__light">Commissions.</span></div>
    <svg class="logo-band" viewBox="0 0 170 90" aria-hidden="true"><path d="M0 90 V40 Q70 -5 170 55 V90 Z" fill="#ffffff"/></svg>
    <p class="brand-name">Harwick Funding Partners</p>
    <p class="call"><span class="call__label">Call</span><span class="call__number">(844) 312-7740</span></p>
    <a class="cta">GET STARTED</a>
  </section>

  <section class="frame frame--three" aria-label="Frame 3">
    <div class="character" role="img" aria-label="Illustrated businessman with glasses and tie, raising three fingers"></div>
    <div class="bubble bubble--people"><span class="bubble__strong">Real</span><span class="bubble__light">People.</span></div>
    <div class="bubble bubble--commissions"><span class="bubble__strong">Competitive</span><span class="bubble__light">Commissions.</span></div>
    <div class="bubble bubble--rates"><span class="bubble__strong">Great</span><span class="bubble__light">Rates.</span></div>
    <svg class="logo-band" viewBox="0 0 170 90" aria-hidden="true"><path d="M0 90 V40 Q70 -5 170 55 V90 Z" fill="#ffffff"/></svg>
    <p class="brand-name">Harwick Funding Partners</p>
    <p class="call"><span class="call__label">Call</span><span class="call__number">(844) 312-7740</span></p>
    <a class="cta">GET STARTED</a>
  </section>

  <p class="frame-label" style="left:33px">FRAME 1</p>
  <p class="frame-label" style="left:418px">FRAME 2</p>
  <p class="frame-label" style="left:803px">FRAME 3</p>

</main>
</body>
</html>
```